I want to redesign the Tallvo corporate website

Brookhill Agro Limited (Tallvo) is a Nigerian integrated agribusiness and premium food company operating across agriculture, food processing and nationwide FMCG distribution.
We are redesigning our corporate website to reflect our evolution into a modern, premium food company capable of serving institutional buyers, distributors, retailers, investors and consumers. The new website should feel comparable to the websites of leading global food brands — not a typical agricultural website.

Target Market(s)

Nigeria / Africa

Industry/Entity Type

FMCG

Coding

Number of Pages Required

5+ page

Colors

Designer to choose colors to be used in the design.

Requirements
Must have
• The website must communicate the following attributes consistently across every page, in both design and language. Premium Quality of finish signals quality of product , Clean Uncluttered layouts, disciplined use of elements ,Modern Current design language, not dated conventions ,Innovative and Forward-looking, technology-enabled , Sustainable Responsible practice made visible Nigerian with global standards, Proudly local in origin, international in execution
Nice to have
• Lots of white space , Fast loading, Premium photography,Mobile-first,Elegant typography,Minimal clutter, Rounded elements,High-end corporate feel, Smooth curved section transitions, Soft shadows
Should not have
• The new website should feel comparable to the websites of leading global food brands — not a typical agricultural website. Also do not copy the business profile as website , its is just a guide !

```html
<!DOCTYPE html>
<html lang="en">
<head>
<meta charset="utf-8">
<title>Tallvo — Integrated Agriculture</title>
<link rel="stylesheet" href="https://fonts.googleapis.com/css2?family=Playfair+Display:wght@500;600;700&family=Montserrat:wght@400;500;600;700&display=swap">
<style>
:root{
  --green:#97c124;
  --green-dark:#6f9a12;
  --green-pale:#eef5dc;
  --ink:#111611;
  --muted:#3a3f38;
  --accent:#e5562a;
  --footer:#112218;
  --white:#ffffff;
  --serif:'Playfair Display', serif;
  --sans:'Montserrat', sans-serif;
}
*{box-sizing:border-box;margin:0;padding:0}
html,body{width:1200px;height:3536px;overflow:hidden;background:var(--white)}
body{position:relative;font-family:var(--sans);color:var(--ink)}
.abs{position:absolute}

/* header */
.brand{font-family:var(--serif);font-weight:700;color:var(--ink);letter-spacing:-1px}
.site-brand{left:0;width:1200px;top:40px;text-align:center;font-size:72px}
.menu-btn{left:1052px;top:18px;width:38px;height:38px;border-radius:50%;background:var(--green);display:flex;align-items:center;justify-content:center}

/* hero */
.hero-title{left:113px;top:206px;font-family:var(--serif);font-weight:500;font-size:62px;line-height:70px;color:var(--ink)}
.hero-sub{left:113px;top:508px;font-size:24px;font-weight:500}
.btn{display:flex;align-items:center;justify-content:center;gap:12px;background:var(--green);color:var(--white);font-family:var(--sans)}
.hero-btn{left:113px;top:570px;width:269px;height:55px;border-radius:0 30px 0 30px;font-size:16px}
.hero-ring{left:571px;top:165px;width:522px;height:522px;border-radius:50%;border:4px solid var(--green);clip-path:inset(0 0 55% 0)}
.hero-photo{left:587px;top:181px;width:490px;height:490px;border-radius:50%;background:radial-gradient(circle at 50% 45%,#d9874e 0%,#b86a35 35%,#8a6a3e 65%,#5c6b3a 100%)}
.field{left:0;top:560px;width:1200px;height:460px;background:linear-gradient(180deg,rgba(255,255,255,1) 0%,#c7d1b5 20%,#8fa274 50%,#6f8a56 100%)}
.partner-panel{left:0;top:752px;width:1200px;height:620px;background:var(--white);border-top-left-radius:275px}

/* partnerships */
.eyebrow{left:113px;top:878px;font-size:17px;font-weight:700;letter-spacing:6px;color:var(--green);display:flex;align-items:center;gap:8px}
.eyebrow::after{content:"";width:36px;height:2px;background:var(--green)}
.partner-title{left:113px;top:903px;font-family:var(--serif);font-weight:600;font-size:42px;color:var(--ink)}
.partner-copy{left:113px;top:974px;width:580px;font-size:11.4px;line-height:19.5px;color:var(--ink)}
.audience{left:113px;top:1073px;width:380px;list-style:none}
.audience li{display:flex;height:35px;align-items:center;border-bottom:1px solid #9a9e98;font-size:14px;font-weight:600}
.audience span{width:55px;color:var(--accent);font-weight:500}
.partner-btn{left:113px;top:1199px;width:217px;height:42px;border-radius:0 14px 0 14px;font-size:13px;font-weight:700}

.enquiry-bg{left:779px;top:862px;width:392px;height:396px;border-radius:50%;background:radial-gradient(circle at 60% 55%,#fbfdf5 0%,#eef5dc 100%)}
.enquiry-label{left:858px;top:930px;font-size:11px;color:var(--green)}
.enquiry-title{left:858px;top:946px;font-family:var(--serif);font-weight:700;font-size:19px}
.field-input{left:858px;width:229px;height:38px;border-radius:0 10px 0 10px;background:linear-gradient(90deg,#e8f0d3,#f7faee);font-size:11px;color:#555;padding:0 14px;display:flex;align-items:center}
.enquiry-btn{left:858px;top:1131px;width:229px;height:43px;border-radius:0 12px 0 12px;font-size:11px;font-weight:500}

/* journey */
.journey{left:0;top:1359px;width:1200px;height:598px;background:var(--green);border-bottom-right-radius:320px}
.journey-title{left:0;top:1444px;width:1200px;text-align:center;font-family:var(--serif);font-weight:600;font-size:44px;color:var(--white)}
.stage-photo{top:1534px;width:211px;height:217px;border-radius:44px 10px 44px 10px}
.stage-line{left:219px;top:1800px;width:762px;height:2px;background:rgba(255,255,255,.8)}
.stage-dot{top:1794px;width:14px;height:14px;border-radius:50%;background:var(--white)}
.stage-icon{top:1774px;width:54px;height:54px;border-radius:50%;background:var(--white);display:flex;align-items:center;justify-content:center}
.stage-label{top:1840px;width:260px;text-align:center;font-size:19px;color:var(--white)}

/* values */
.values-bg{left:173px;top:2061px;width:456px;height:456px;border-radius:50%;background:radial-gradient(circle at 60% 60%,#ffffff 0%,#eef5dc 100%)}
.values-brand{left:173px;top:2232px;width:456px;text-align:center;font-size:100px}
.value-pill{height:64px;width:200px;border-radius:0 32px 32px 0;background:linear-gradient(90deg,#f4f4f4,#e4e4e4);box-shadow:4px 6px 10px rgba(0,0,0,.15);font-size:12.5px;font-weight:700;display:flex;align-items:center;justify-content:center;padding:0 12px 0 74px;white-space:nowrap}
.value-hex{width:100px;height:100px}
.value-node{width:14px;height:14px}

/* products */
.products-bg{left:0;top:2600px;width:1200px;height:565px;background:linear-gradient(180deg,#ffffff 0%,#f9fbf1 100%)}
.section-title{left:0;width:1200px;text-align:center;font-family:var(--serif);font-weight:700;font-size:42px;color:var(--ink)}
.product-card{top:2750px;width:308px;height:323px;border-radius:26px;background:var(--white);box-shadow:0 8px 24px rgba(60,80,20,.06);overflow:hidden}
.product-photo{height:243px;width:100%}
.product-name{height:80px;display:flex;align-items:center;justify-content:space-between;padding:0 20px;font-size:21px;font-weight:500}
.go{width:30px;height:30px;flex:none;border-radius:50%;background:var(--green);display:flex;align-items:center;justify-content:center}

.cta-btn{left:489px;top:3265px;width:222px;height:55px;border-radius:0 22px 0 22px;font-size:18px;font-weight:500}

/* footer */
.site-footer{left:0;top:3368px;width:1200px;height:168px;background:var(--footer);color:var(--white)}
.footer-brand{left:113px;top:42px;font-size:56px;color:var(--white)}
.footer-tag{left:349px;top:70px;font-size:11px;line-height:21px}
.footer-rule{top:50px;width:1px;height:74px;background:#2f6b33}
.footer-links{top:58px;list-style:none;font-size:11px;line-height:21.5px}
.footer-links li::before{content:"";display:inline-block;width:7px;height:3px;border-radius:2px;background:var(--green);margin-right:8px;vertical-align:middle}
.footer-leaf{left:960px;top:38px;width:140px;height:110px;border-radius:60px 0 60px 0;background:linear-gradient(135deg,rgba(151,193,36,.12),rgba(151,193,36,0))}
</style>
</head>
<body>

<header>
  <div class="abs brand site-brand">Tallvo</div>
  <div class="abs menu-btn" aria-label="Menu">
    <svg width="18" height="14" viewBox="0 0 18 14"><path d="M1 1h16M1 7h16M5 13h12" stroke="#111" stroke-width="2" stroke-linecap="round"/></svg>
  </div>
</header>

<section class="hero">
  <div class="abs field" role="img" aria-label="Misty rows of green crops stretching to the horizon"></div>
  <h1 class="abs hero-title">INTEGRATED<br>AGRICULTURE.<br>NOURISHING<br>LIVES.</h1>
  <p class="abs hero-sub">From our farms to every table.</p>
  <a class="abs btn hero-btn">Explore our products
    <svg width="24" height="12" viewBox="0 0 24 12"><path d="M1 6h21M17 1l5 5-5 5" stroke="#fff" stroke-width="1.6" fill="none"/></svg>
  </a>
  <div class="abs hero-ring"></div>
  <div class="abs hero-photo" role="img" aria-label="Tallvo product range: brown egg trays, honey jar and plantain chip packs on a table"></div>
</section>

<section class="partnerships">
  <div class="abs partner-panel"></div>
  <p class="abs eyebrow">PARTNERSHIPS</p>
  <h2 class="abs partner-title">Let’s grow good business together.</h2>
  <p class="abs partner-copy">From dependable institutional supply to nationwide distribution, Tallvo works with ambitious partners to make premium Nigerian food more accessible. Through consistent quality, reliable logistics and flexible support, we help buyers, distributors and collaborators reach new markets, serve more customers and bring trusted Nigerian flavours to more tables.</p>
  <ul class="abs audience">
    <li><span>01</span>Institutional buyers</li>
    <li><span>02</span>Distributors &amp; retailers</li>
    <li><span>03</span>Investors &amp; collaborators</li>
  </ul>
  <a class="abs btn partner-btn">START A CONVERSATION →</a>

  <div class="abs enquiry-bg"></div>
  <p class="abs enquiry-label">PARTNER ENQUIRY</p>
  <h3 class="abs enquiry-title">Tell us how to reach you.</h3>
  <div class="abs field-input" style="top:979px">Your Name</div>
  <div class="abs field-input" style="top:1029px">Phone Number</div>
  <div class="abs field-input" style="top:1079px">Work Email</div>
  <a class="abs btn enquiry-btn">START THE CONVERSATION ↗</a>
</section>

<section class="journey-section">
  <div class="abs journey"></div>
  <h2 class="abs journey-title">From source to shelf</h2>
  <div class="abs stage-photo" style="left:113px;background:linear-gradient(180deg,#9cc4e0 0%,#6f9a3a 30%,#2f5a1c 100%)" role="img" aria-label="Rows of leafy crops in a field"></div>
  <div class="abs stage-photo" style="left:367px;background:linear-gradient(160deg,#6b4a2e,#3d2a1a 60%,#5a6f8a)" role="img" aria-label="Smiling farmer in a straw hat in a poultry house"></div>
  <div class="abs stage-photo" style="left:622px;background:linear-gradient(160deg,#8a8f94,#c97a3a 55%,#5a5e62)" role="img" aria-label="Eggs moving along a processing conveyor"></div>
  <div class="abs stage-photo" style="left:876px;background:linear-gradient(160deg,#8a5a34,#c8a040 45%,#b03a2e)" role="img" aria-label="Plantain chip packs and egg trays on a store shelf"></div>

  <div class="abs stage-line"></div>
  <div class="abs stage-dot" style="left:338px"></div>
  <div class="abs stage-dot" style="left:592px"></div>
  <div class="abs stage-dot" style="left:847px"></div>

  <div class="abs stage-icon" style="left:191px"><svg width="30" height="30" viewBox="0 0 30 30" fill="none" stroke="#333" stroke-width="1.5"><path d="M15 27V14M15 16C15 9 9 6 4 7c0 6 4 9 11 9zM15 14c0-6 5-9 11-8 0 6-5 9-11 8z"/></svg></div>
  <div class="abs stage-icon" style="left:446px"><svg width="30" height="30" viewBox="0 0 30 30" fill="none" stroke="#333" stroke-width="1.5"><circle cx="9" cy="11" r="3"/><circle cx="21" cy="11" r="3"/><circle cx="15" cy="15" r="3"/><path d="M4 24c0-4 2-7 5-7M26 24c0-4-2-7-5-7M9 26c0-4 3-7 6-7s6 3 6 7"/></svg></div>
  <div class="abs stage-icon" style="left:700px"><svg width="30" height="30" viewBox="0 0 30 30" fill="none" stroke="#333" stroke-width="1.5"><circle cx="15" cy="11" r="6"/><path d="M3 16l4 9h6M27 16l-4 9h-6M9 19c2 1 4 2 6 2s4-1 6-2"/></svg></div>
  <div class="abs stage-icon" style="left:954px"><svg width="30" height="30" viewBox="0 0 30 30" fill="none" stroke="#333" stroke-width="1.5"><path d="M2 6h4l3 13h15l3-9H8"/><circle cx="11" cy="24" r="2"/><circle cx="22" cy="24" r="2"/><path d="M12 13h11M13 16h9"/></svg></div>

  <p class="abs stage-label" style="left:89px">Carefully grown</p>
  <p class="abs stage-label" style="left:343px">Expertly raised</p>
  <p class="abs stage-label" style="left:597px">Responsibly processed</p>
  <p class="abs stage-label" style="left:851px">Thoughtfully delivered</p>
</section>

<section class="values">
  <div class="abs values-bg"></div>
  <div class="abs brand values-brand">Tallvo</div>

  <svg class="abs" style="left:680px;top:2070px" width="120" height="450" viewBox="0 0 120 450" fill="none">
    <path d="M30 10 L8 46 L30 82 L90 90 L96 156 L70 180 L30 195 L8 268 L30 300 L90 310 L96 376 L70 400 L40 440" stroke="#555" stroke-width="1.2" stroke-dasharray="4 4"/>
  </svg>

  <svg class="abs value-node" style="left:681px;top:2109px" viewBox="0 0 14 14"><polygon points="7,0 13,3.5 13,10.5 7,14 1,10.5 1,3.5" fill="#111"/></svg>
  <svg class="abs value-node" style="left:770px;top:2219px" viewBox="0 0 14 14"><polygon points="7,0 13,3.5 13,10.5 7,14 1,10.5 1,3.5" fill="#111"/></svg>
  <svg class="abs value-node" style="left:684px;top:2330px" viewBox="0 0 14 14"><polygon points="7,0 13,3.5 13,10.5 7,14 1,10.5 1,3.5" fill="#111"/></svg>
  <svg class="abs value-node" style="left:767px;top:2440px" viewBox="0 0 14 14"><polygon points="7,0 13,3.5 13,10.5 7,14 1,10.5 1,3.5" fill="#111"/></svg>

  <div class="abs value-pill" style="left:750px;top:2084px">COMMUNITY</div>
  <div class="abs value-pill" style="left:838px;top:2194px">EDUCATION</div>
  <div class="abs value-pill" style="left:750px;top:2305px">SUSTAINABILITY</div>
  <div class="abs value-pill" style="left:838px;top:2415px">WELL-BEING</div>

  <svg class="abs value-hex" style="left:722px;top:2066px" viewBox="0 0 100 100"><polygon points="28,3 72,3 97,50 72,97 28,97 3,50" fill="#7fa818"/><polygon points="32,12 68,12 88,50 68,88 32,88 12,50" fill="#97c124"/><g fill="none" stroke="#fff" stroke-width="1.8"><circle cx="50" cy="44" r="12"/><path d="M34 68v-8M42 68v-6M50 68v-7M58 68v-6M66 68v-8M30 68h40"/></g></svg>
  <svg class="abs value-hex" style="left:810px;top:2176px" viewBox="0 0 100 100"><polygon points="28,3 72,3 97,50 72,97 28,97 3,50" fill="#7fa818"/><polygon points="32,12 68,12 88,50 68,88 32,88 12,50" fill="#97c124"/><g fill="none" stroke="#fff" stroke-width="1.8"><rect x="32" y="30" width="36" height="22" rx="2"/><path d="M38 38h14M38 44h20"/><circle cx="42" cy="60" r="4"/><circle cx="58" cy="60" r="4"/><path d="M34 72c0-5 4-7 8-7s8 2 8 7M50 72c0-5 4-7 8-7s8 2 8 7"/></g></svg>
  <svg class="abs value-hex" style="left:722px;top:2287px" viewBox="0 0 100 100"><polygon points="28,3 72,3 97,50 72,97 28,97 3,50" fill="#7fa818"/><polygon points="32,12 68,12 88,50 68,88 32,88 12,50" fill="#97c124"/><g fill="none" stroke="#fff" stroke-width="1.8"><circle cx="48" cy="52" r="16"/><path d="M38 44c5 2 6 6 4 10M54 40c-2 5 2 8 8 8M58 32c6-4 12-2 14 2-4 4-10 4-14-2z"/></g></svg>
  <svg class="abs value-hex" style="left:810px;top:2397px" viewBox="0 0 100 100"><polygon points="28,3 72,3 97,50 72,97 28,97 3,50" fill="#7fa818"/><polygon points="32,12 68,12 88,50 68,88 32,88 12,50" fill="#97c124"/><g fill="none" stroke="#fff" stroke-width="1.8"><circle cx="50" cy="40" r="5"/><path d="M50 46v14M38 50l12 10 12-10M32 66c8 4 28 4 36 0M40 30l-3-4M60 30l3-4M50 28v-5"/></g></svg>
</section>

<section class="products">
  <div class="abs products-bg"></div>
  <h2 class="abs section-title" style="top:2670px">FROM SOURCE TO SHELF</h2>

  <article class="abs product-card" style="left:113px">
    <div class="product-photo" style="background:radial-gradient(circle at 45% 55%,#d98a4e 0%,#b0622e 45%,#6e4a2e 100%)" role="img" aria-label="Brown eggs in a wooden bowl"></div>
    <div class="product-name">Premium Brown Eggs <span class="go"><svg width="14" height="14" viewBox="0 0 14 14"><path d="M2 7h10M8 3l4 4-4 4" stroke="#fff" stroke-width="1.8" fill="none"/></svg></span></div>
  </article>
  <article class="abs product-card" style="left:446px">
    <div class="product-photo" style="background:radial-gradient(circle at 55% 45%,#e3a43c 0%,#b77a2a 45%,#4f5a2c 100%)" role="img" aria-label="Bowl of crispy plantain chips"></div>
    <div class="product-name">Crispy Plantain Chips <span class="go"><svg width="14" height="14" viewBox="0 0 14 14"><path d="M2 7h10M8 3l4 4-4 4" stroke="#fff" stroke-width="1.8" fill="none"/></svg></span></div>
  </article>
  <article class="abs product-card" style="left:779px">
    <div class="product-photo" style="background:radial-gradient(circle at 45% 50%,#c9761e 0%,#9a5412 45%,#d8cdb0 100%)" role="img" aria-label="Jar of pure honey with a honey dipper"></div>
    <div class="product-name">Pure Honey <span class="go"><svg width="14" height="14" viewBox="0 0 14 14"><path d="M2 7h10M8 3l4 4-4 4" stroke="#fff" stroke-width="1.8" fill="none"/></svg></span></div>
  </article>
</section>

<section class="cta">
  <h2 class="abs section-title" style="top:3205px">FROM SOURCE TO SHELF</h2>
  <a class="abs btn cta-btn" style="color:var(--ink)">Partner with us
    <svg width="22" height="12" viewBox="0 0 22 12"><path d="M1 6h19M15 1l5 5-5 5" stroke="#111" stroke-width="1.6" fill="none"/></svg>
  </a>
</section>

<footer class="abs site-footer">
  <div class="abs brand footer-brand">Tallvo</div>
  <p class="abs footer-tag">Good for you.<br>Good for the planet.</p>
  <div class="abs footer-rule" style="left:529px"></div>
  <ul class="abs footer-links" style="left:604px">
    <li>Home</li><li>About</li><li>Products</li>
  </ul>
  <div class="abs footer-rule" style="left:737px"></div>
  <ul class="abs footer-links" style="left:813px">
    <li>Our business</li><li>Sustainability</li><li>Contact</li>
  </ul>
  <div class="abs footer-leaf" role="img" aria-label="Faint leaf decoration"></div>
</footer>

</body>
</html>
```